Freelance business trainer needs a new business card

My business is called Varnholt. I provide training in the workplace on management, coaching and mentoring, and customer service topics for a variety of businesses, colleges and private training providers, and teach on management programs. I need a professional but eye catching business card. Business colours grey and orange. My name Linda Marrowby; Tel 07700 900417; email lmarrowby@varnholt.example; website www.varnholt.example.
Happy to have some sort of logo on front and details on back or all on one side
Target Market(s)
SME businesses and colleges - workshops i run are for adults in the workplace
Industry/Entity Type
Training
Look and feel
Each slider illustrates characteristics of the customer's brand and the style your logo design should communicate.

```html
<!DOCTYPE html>
<html lang="en">
<head>
<meta charset="utf-8">
<title>Varnholt – Business Card</title>
<link rel="stylesheet" href="https://fonts.googleapis.com/css2?family=Jost:wght@400&display=swap">
<style>
  :root {
    --brand-orange: #e07a2e;
    --brand-grey: #6d6e70;
    --ink: #262626;
    --paper: #ffffff;
    --frame: #c8c8c8;
  }
  html, body {
    margin: 0;
    padding: 0;
    overflow: hidden;
    background: var(--paper);
  }
  .card {
    position: relative;
    width: 1200px;
    height: 734px;
    box-sizing: border-box;
    border: 2px solid var(--frame);
    background: var(--paper);
    font-family: "Jost", "Futura", sans-serif;
    color: var(--ink);
    overflow: hidden;
  }
  .brand {
    position: absolute;
    left: 100px;
    top: 107px;
    display: flex;
    align-items: center;
    gap: 12px;
  }
  .brand-dot {
    width: 142px;
    height: 142px;
    border-radius: 50%;
    background: var(--brand-grey);
  }
  .brand-name {
    font-size: 100px;
    font-weight: 400;
    letter-spacing: 3px;
    text-transform: uppercase;
    color: var(--brand-orange);
    line-height: 1;
  }
  .holder-name {
    position: absolute;
    left: 671px;
    top: 358px;
    margin: 0;
    font-size: 52px;
    font-weight: 400;
    letter-spacing: 3px;
    line-height: 1;
  }
  .address {
    position: absolute;
    left: 101px;
    top: 518px;
    margin: 0;
    font-style: normal;
    font-size: 34px;
    line-height: 46.5px;
  }
  .contacts {
    position: absolute;
    left: 674px;
    top: 516px;
    margin: 0;
    padding: 0;
    list-style: none;
    font-size: 33px;
    letter-spacing: 1px;
  }
  .contact {
    display: flex;
    align-items: center;
    height: 47px;
  }
  .contact-icon {
    width: 38px;
    height: 38px;
    margin-right: 24px;
    fill: var(--brand-orange);
    stroke: var(--brand-orange);
  }
</style>
</head>
<body>
  <main class="card">
    <div class="brand">
      <span class="brand-dot"></span>
      <span class="brand-name">Varnholt</span>
    </div>

    <h1 class="holder-name">Linda Marrowby</h1>

    <address class="address">
      Address can come here<br>
      Address can come here<br>
      Address can come here
    </address>

    <ul class="contacts">
      <li class="contact">
        <svg class="contact-icon" viewBox="0 0 38 38" aria-hidden="true">
          <rect x="9" y="2" width="20" height="34" rx="4" stroke="none"/>
          <rect x="12" y="6" width="14" height="22" rx="1" fill="#fff" stroke="none"/>
          <circle cx="19" cy="32" r="1.8" fill="#fff" stroke="none"/>
        </svg>
        <span>07700 900417</span>
      </li>
      <li class="contact">
        <svg class="contact-icon" viewBox="0 0 38 38" aria-hidden="true">
          <rect x="2" y="8" width="34" height="22" rx="1" stroke="none"/>
          <path d="M3 9 L19 22 L35 9" fill="none" stroke="#fff" stroke-width="2"/>
          <path d="M3 29 L14 18 M35 29 L24 18" fill="none" stroke="#fff" stroke-width="1.6"/>
        </svg>
        <span>lmarrowby@varnholt.example</span>
      </li>
      <li class="contact">
        <svg class="contact-icon" viewBox="0 0 38 38" aria-hidden="true">
          <circle cx="19" cy="19" r="15" stroke="none"/>
          <g fill="none" stroke="#fff" stroke-width="2">
            <ellipse cx="19" cy="19" rx="6.5" ry="14"/>
            <line x1="19" y1="5" x2="19" y2="33"/>
            <line x1="5" y1="19" x2="33" y2="19"/>
            <path d="M8 11.5 H30 M8 26.5 H30"/>
          </g>
        </svg>
        <span>www.varnholt.example</span>
      </li>
    </ul>
  </main>
</body>
</html>
```